Online religious stickers company needs a letterhead design

I need a letterhead design for a startup internet company that sells religious stickers and magnets. I would like to see a design that incorporates the color blue any shade of blue is fine. Maybe the use of very light clouds signifying heaven but it is not necessary. I am attaching my logo the color can be changed if necessary.
I do not want something that is very busy. Simple is better.

Religious

```html
<!DOCTYPE html>
<html lang="en">
<head>
<meta charset="utf-8">
<title>Skyward Letterhead</title>
<link href="https://fonts.googleapis.com/css2?family=Nunito+Sans:wght@400;800&display=swap" rel="stylesheet">
<style>
  :root {
    --paper: #ffffff;
    --sky-deep: #0b4f80;
    --sky-mid: #17689c;
    --sky-glow: #2596d1;
    --rim: #1aa9e8;
    --cloud-soft: #c9d8ef;
    --cloud-left: #a3b4de;
    --ink-navy: #1e3f86;
    --frame: #ffffff;
  }
  html, body {
    margin: 0;
    padding: 0;
    overflow: hidden;
    background: var(--paper);
  }
  .letterhead {
    position: relative;
    width: 927px;
    height: 1200px;
    background: var(--paper);
    overflow: hidden;
    font-family: "Nunito Sans", "Avenir", sans-serif;
  }
  .sky-wash {
    position: absolute;
  }
  .sky-wash--left {
    left: 10px;
    top: 105px;
    width: 165px;
    height: 95px;
    background: radial-gradient(ellipse at 60% 60%, var(--cloud-left) 0%, rgba(163, 180, 222, 0.6) 45%, rgba(163, 180, 222, 0) 72%);
  }
  .sky-wash--right {
    left: 560px;
    top: 78px;
    width: 367px;
    height: 225px;
    background: radial-gradient(ellipse at 45% 45%, var(--cloud-soft) 0%, rgba(201, 216, 239, 0.65) 45%, rgba(201, 216, 239, 0) 72%);
  }
  .letterhead__art {
    position: absolute;
    inset: 0;
    width: 927px;
    height: 1200px;
    display: block;
  }
  .brand-name {
    position: absolute;
    left: 386px;
    top: 112px;
    transform: translateX(-50%);
    margin: 0;
    font-weight: 800;
    font-size: 56px;
    letter-spacing: 1px;
    line-height: 1;
    color: var(--frame);
  }
  .contact {
    position: absolute;
    right: 54px;
    top: 56px;
    margin: 0;
    text-align: right;
    font-style: normal;
    color: var(--ink-navy);
    line-height: 1.25;
  }
  .contact__street,
  .contact__city {
    display: block;
    font-size: 19px;
    letter-spacing: 0.3px;
  }
  .contact__phone,
  .contact__web {
    display: block;
    font-size: 15.5px;
    line-height: 1.35;
  }
</style>
</head>
<body>
<div class="letterhead">
  <div class="sky-wash sky-wash--left" role="img" aria-label="Soft light clouds illustration"></div>
  <div class="sky-wash sky-wash--right" role="img" aria-label="Soft light clouds illustration"></div>

  <svg class="letterhead__art" viewBox="0 0 900 1165" preserveAspectRatio="none" aria-hidden="true">
    <defs>
      <radialGradient id="skyFill" cx="430" cy="1085" r="1050" gradientUnits="userSpaceOnUse">
        <stop offset="0" stop-color="var(--sky-glow)"/>
        <stop offset="0.45" stop-color="var(--sky-mid)"/>
        <stop offset="1" stop-color="var(--sky-deep)"/>
      </radialGradient>
    </defs>

    <path class="panel-rim" fill="none" stroke="var(--rim)" stroke-width="24"
      d="M0,195 Q70,180 150,200 C160,100 250,32 375,32 C500,32 580,100 600,185 Q700,150 790,192 C822,215 842,262 856,305 Q880,300 900,312 L900,1165 L0,1165 Z"/>
    <path class="panel" fill="url(#skyFill)"
      d="M0,195 Q70,180 150,200 C160,100 250,32 375,32 C500,32 580,100 600,185 Q700,150 790,192 C822,215 842,262 856,305 Q880,300 900,312 L900,1165 L0,1165 Z"/>

    <path class="writing-frame" fill="none" stroke="var(--frame)" stroke-width="3"
      d="M39,185 V1112 H861 V310"/>
  </svg>

  <p class="brand-name">SKYWARD</p>

  <address class="contact">
    <span class="contact__street">5678 Meadowlark Ln.</span>
    <span class="contact__city">Springvale, NJ 00222</span>
    <span class="contact__phone">1 (800) 555-0142</span>
    <span class="contact__web">www.skywardstickers.com</span>
  </address>
</div>
</body>
</html>
```